4x6 postcard design Tide And Time

A full color double sided postcard 4x6 postcard. I have attached a screenshot of the text that should be used on the postcard. The front is titled this is the front. The back is titled the back. REMEMBER THE screenshots are used to show you the text. Please design using your own creative methods. The color scheme should remain pretty similar to the screenshot.

On the front of the card, I'd like to add a 4th bullet (or check) that says This is NOT cash gifting!
Also on the front, add a line that says call 877-402-3915 or send an email to join@tideandtimeco.net and mention ID#:

On the back, please add a line that says call 877-402-3915 or send an email to join@tideandtimeco.net and mention ID#:

On the front OR back it should say 100% Satisfaction Guarantee

Target Market(s)

work from home

Font styles to use
Sans Serif

Requirements
Must have
• The correct text on both sides. Please read the directions carefully.
Nice to have
• A very creative, attention-grabbing design. The 100% Satisfaction Guarantee designed in a way that looks like the gold seals that pop up if you google "money back guarantee seal"

```html
<!DOCTYPE html>
<html lang="en">
<head>
<meta charset="utf-8">
<title>Tide And Time Postcard</title>
<link rel="stylesheet" href="https://fonts.googleapis.com/css2?family=Oswald:wght@300;400;500;600;700&family=Montserrat:wght@800&family=Questrial&family=Sacramento&display=swap">
<style>
:root{
  --green:#11924a;
  --gold:#e8ac2c;
  --gold-dark:#d99a1b;
  --ink:#1d1d1d;
  --grey-panel:#d8d9da;
  --paper:#ffffff;
  --backdrop:#e9e7e4;
}
*{box-sizing:border-box;margin:0;padding:0}
html,body{width:847px;height:1200px;overflow:hidden;background:var(--backdrop)}
body{position:relative;font-family:'Oswald',sans-serif;color:var(--ink)}
.card{position:absolute;left:60px;width:726px;height:484px;background:var(--paper);overflow:hidden;box-shadow:0 4px 14px rgba(0,0,0,.18)}
.front{top:53px}
.back{top:656px}
.abs{position:absolute}

/* front */
.photo{left:0;top:0;width:412px;height:372px;background:linear-gradient(160deg,#ffffff 0%,#f1ece8 35%,#8a5a44 55%,#2c2a2d 75%,#d9dcdf 100%)}
.brand{left:26px;top:26px;width:136px;height:136px;border-radius:50%;background:var(--paper);border:5px solid var(--gold);display:flex;align-items:center;justify-content:center;text-align:center;font-weight:600;font-size:22px;line-height:1.05;color:var(--green)}
.band{left:0;top:350px;width:420px;height:134px}
.call-label{left:52px;top:382px;width:308px;display:flex;align-items:center;gap:8px;color:#fff;font-size:17px;font-weight:400}
.call-label::before,.call-label::after{content:"";flex:1;height:1px;background:rgba(255,255,255,.7)}
.phone{left:52px;top:400px;display:flex;align-items:center;gap:10px;color:#fff;font-weight:700;font-size:42px;letter-spacing:2.5px;line-height:1;white-space:nowrap}
.email-line{left:56px;top:454px;color:#fff;font-size:10.5px;font-weight:300;white-space:nowrap}
.email-line b{color:var(--gold);font-weight:400}
.id-slot{display:inline-block;width:58px;height:11px;background:#fff;vertical-align:middle;margin-left:4px}

.headline-dont{left:425px;top:18px;font-size:80px;font-weight:700;color:var(--green);line-height:1;letter-spacing:-1px}
.headline-pro{left:426px;top:100px;font-size:40px;font-weight:700;color:var(--gold);line-height:1;letter-spacing:-.6px;white-space:nowrap}
.rule{left:425px;top:153px;width:276px;height:1px;background:var(--gold)}
.pitch{left:428px;top:158px;width:280px;font-family:'Questrial',sans-serif;font-size:14.5px;line-height:17px;white-space:nowrap}
.script{left:546px;top:192px;font-family:'Sacramento',cursive;font-size:34px;color:var(--gold);line-height:1;white-space:nowrap}
.thousands{left:424px;top:232px;font-size:42px;font-weight:700;color:var(--gold);letter-spacing:4px;line-height:1;white-space:nowrap}

.promise-box{left:419px;top:315px;width:320px;height:134px;border:2px solid var(--gold);border-right:none}
.seal{left:422px;top:283px;width:62px;height:62px;border-radius:50%;background:var(--green);border:3px solid #fff;box-shadow:0 0 0 2px var(--green);color:#fff;font-weight:500;font-size:22px;display:flex;align-items:center;justify-content:center;letter-spacing:-.5px}
.ribbon{left:478px;top:295px;width:130px;height:38px;background:var(--gold);clip-path:polygon(0 0,100% 0,93% 100%,0 100%);color:#fff;font-family:'Montserrat',sans-serif;font-weight:800;font-size:12px;line-height:13px;padding:6px 0 0 14px}
.perks{left:445px;top:348px;list-style:none;font-size:13px;font-weight:300;letter-spacing:-.3px}
.perks li{display:flex;align-items:center;gap:7px;height:23.3px;white-space:nowrap}
.perks b{font-weight:700}
.signup-strip{left:420px;top:448px;width:306px;height:36px;background:var(--green)}
.signup-text{right:9px;top:452px;color:#fff;font-weight:600;font-size:20px;letter-spacing:-.3px}

/* back */
.panel{left:0;top:0;width:369px;height:484px;background:var(--grey-panel)}
.question{left:0;top:28px;width:330px;height:42px;background:var(--gold);clip-path:polygon(0 0,100% 0,94% 100%,0 100%);color:#fff;font-weight:600;font-size:21px;letter-spacing:-.7px;padding:2px 0 0 26px;line-height:38px;white-space:nowrap}
.intro{left:29px;top:84px;width:310px;font-size:15.5px;font-weight:300;line-height:20px;text-align:justify;color:#333}
.intro b{font-weight:500}
.steps{left:54px;top:178px;width:290px;list-style:none;font-size:15.5px;font-weight:300;line-height:19px;color:#333}
.steps li{display:flex;gap:6px;margin-bottom:9px}
.steps .num{flex:none;width:14px;height:14px;border-radius:50%;background:var(--gold);color:#fff;font-size:9px;font-weight:600;line-height:14px;text-align:center;margin-top:3px}
.cash-note{left:32px;top:312px;width:300px;font-size:15px;font-weight:400;line-height:18px;letter-spacing:-.3px}
.black-bar{left:0;top:360px;width:369px;height:30px;background:#000;color:#fff;font-size:14.5px;font-weight:500;padding-left:30px;line-height:30px;letter-spacing:-.2px}
.gold-block{left:0;top:390px;width:369px;height:94px;background:var(--gold);color:#fff;font-size:14px;font-weight:400;padding:14px 0 0 30px;line-height:22px;letter-spacing:-.2px}
.gold-block .id-slot{width:84px;height:14px}
.stamp{left:627px;top:32px;width:74px;height:72px;border:1px solid #555}
.address-line{left:457px;width:244px;height:1px;background:#444}
</style>
</head>
<body>

<section class="card front">
  <div class="abs photo" role="img" aria-label="Photo of a smiling businesswoman typing on a laptop at a white desk"></div>
  <div class="abs brand">Tide<br>And<br>Time</div>

  <svg class="abs band" viewBox="0 0 420 134" width="420" height="134" aria-hidden="true">
    <path d="M0 20 Q210 8 420 16 L420 134 L0 134 Z" fill="#e8ac2c"/>
    <path d="M0 25 Q210 13 420 21 L420 134 L0 134 Z" fill="#11924a"/>
  </svg>
  <div class="abs call-label">CALL US AT:</div>
  <div class="abs phone">
    <svg width="28" height="28" viewBox="0 0 24 24" aria-hidden="true"><path d="M6.6 10.8a15.1 15.1 0 006.6 6.6l2.2-2.2a1 1 0 011-.25 11.4 11.4 0 003.6.57 1 1 0 011 1V20a1 1 0 01-1 1A17 17 0 013 4a1 1 0 011-1h3.5a1 1 0 011 1c0 1.25.2 2.45.57 3.57a1 1 0 01-.25 1z" fill="#e8ac2c"/><path d="M14 3a7 7 0 017 7M14 6.5A3.5 3.5 0 0117.5 10" stroke="#e8ac2c" stroke-width="1.8" fill="none"/></svg>
    <span>877-402-3915</span>
  </div>
  <div class="abs email-line">or send an email to <b>join@tideandtimeco.net</b> and mention ID#: <span class="id-slot"></span></div>

  <div class="abs headline-dont">DON’T</div>
  <div class="abs headline-pro">PROCRASTINATE</div>
  <div class="abs rule"></div>
  <p class="abs pitch">People just like you are averaging over<br>$30,000 per month with our quick<br>and easy system.</p>
  <div class="abs script">Start Earning</div>
  <div class="abs thousands">THOUSANDS</div>

  <div class="abs promise-box"></div>
  <div class="abs ribbon">GUARANTEED<br>SATISFACTION</div>
  <div class="abs seal">100%</div>
  <ul class="abs perks">
    <li><svg width="10" height="10" viewBox="0 0 10 10" aria-hidden="true"><rect x=".5" y="1.5" width="7" height="7" fill="none" stroke="#e8ac2c"/><path d="M2.5 5l2 2 4.5-5.5" stroke="#e8ac2c" stroke-width="1.3" fill="none"/></svg><span>We close all your sales for you... Earn money 24 hours a day!</span></li>
    <li><svg width="10" height="10" viewBox="0 0 10 10" aria-hidden="true"><rect x=".5" y="1.5" width="7" height="7" fill="none" stroke="#e8ac2c"/><path d="M2.5 5l2 2 4.5-5.5" stroke="#e8ac2c" stroke-width="1.3" fill="none"/></svg><span>Done-for-you Marketing System</span></li>
    <li><svg width="10" height="10" viewBox="0 0 10 10" aria-hidden="true"><rect x=".5" y="1.5" width="7" height="7" fill="none" stroke="#e8ac2c"/><path d="M2.5 5l2 2 4.5-5.5" stroke="#e8ac2c" stroke-width="1.3" fill="none"/></svg><span>Real Products that pay “Gigantic” cash commisions!</span></li>
    <li><svg width="10" height="10" viewBox="0 0 10 10" aria-hidden="true"><rect x=".5" y="1.5" width="7" height="7" fill="none" stroke="#e8ac2c"/><path d="M2.5 5l2 2 4.5-5.5" stroke="#e8ac2c" stroke-width="1.3" fill="none"/></svg><span>This is <b>NOT</b> cash gifting!</span></li>
  </ul>
  <div class="abs signup-strip"></div>
  <div class="abs signup-text">SIGN UP NOW!</div>
</section>

<section class="card back">
  <div class="abs panel"></div>
  <h2 class="abs question">What is a courseware distributor?</h2>
  <p class="abs intro">A Courseware Distributor is someone such as yourself that joins <b>Tide And Time</b>, and earns thousands of dollars in cash commissions each week. All you have to do is follow 3 simple steps to change your financial health forever:</p>
  <ol class="abs steps">
    <li><span class="num">1</span><span>Call or email right away to join</span></li>
    <li><span class="num">2</span><span>Allow our attention-grabbing postcards or sales letters to work for you to get sales while you sleep.</span></li>
    <li><span class="num">3</span><span>Sit back and let our trained professionals answer your calls and close your sales.</span></li>
  </ol>
  <p class="abs cash-note">Your CASH commision will arrive at your door via Overnight Courier, 6 days per week.</p>
  <div class="abs black-bar">SIGN UP NOW! - 100% GUARANTEED SATISFACTION</div>
  <div class="abs gold-block">
    call 877-402-3915<br>
    or send an email to join@tideandtimeco.net<br>
    and mention ID#: <span class="id-slot"></span>
  </div>

  <div class="abs stamp"></div>
  <div class="abs address-line" style="top:190px"></div>
  <div class="abs address-line" style="top:219px"></div>
  <div class="abs address-line" style="top:248px"></div>
  <div class="abs address-line" style="top:278px"></div>
</section>

</body>
</html>
```